Photography Prints Business Card Design

Background info: Nature, flower, landscape,  macro, wildlife photographer. Shoot color and B&W images. Sell prints at juried fine art shows.
Looking for two-sided, clean, memorable design with creative use of my initials, DH.   I like the DH symbol in the my logo. Just use the DH symbol. Do not leave the underlying text as uploaded by me. I do not like the serif font and positioning of the words!  Either  remove the small print "Dorian Hallet Photography" under the logo,  or change to a sans serif font, or reposition with "Dorian Hallet" above "Photography" which seems to work with serif fonts.
Target Market(s)
Sophisticated art buyers, post-college to middle age
Industry/Entity Type
Business
Contact Information for Business Card
Dorian Hallet Photography
728 Maple Brook CT
Cedar Hollow, NC 27999
(555) 555-0148
www.dorianhallet.com
CP:halletphoto
dorian@dorianhallet.com
If using just one line address, make sure there is a comma after  "CT" in street address. For example:
728 Maple Brook CT, Cedar Hollow, NC 27999
Requirements
Must have
- 1.Two-sided card submitted as one design.
2. Must use the DH symbol in my logo.
3. Do not leave the text "Dorian Hallet Photography" under the DH symbol in the logo uploaded by me. I do not like that serif font or the positioning of the words! Either remove the small print "Dorian Hallet Photography" under the logo entirely, or change text to a sans serif font, or reposition text with "Dorian Hallet" above "Photography" which seems to work with serif fonts.
Nice to have
- Can use my DH logo (three file types uploaded: AI, PSD, TIF)  I  like the attached B&W water droplet photo.  My pictures on my website, www.dorianhhallet.com  can also be used.  Possible use of Chirply logo with (either the "f" alone or the square blue icon with white "f") my CP page short url name: halletphoto.
Should not have
- 1.No icons or pictures  of camera or lenses or other photographic gear or film strips.
2. No QR or other "barcode" type symbols.
3. No outlining of my logo symbol (drop shadow possibly).
4. No decorative or outlined fonts.
5. I am not a fan of most script fonts.
6. No play on "Hallet" such as snow or other winter season symbols.
7. Do not keep the original text, "Dorian Hallet Photography" under DH logo. Change it or remove it entirely.

```html
<!DOCTYPE html>
<html lang="en">
<head>
<meta charset="utf-8">
<title>Dorian Hallet Photography — Business Card</title>
<link rel="stylesheet" href="https://fonts.googleapis.com/css2?family=Michroma&display=swap">
<style>
  :root {
    --page: #d6d6d9;
    --card-grey-light: #e4e4e6;
    --card-grey-mid: #b9b9bc;
    --magenta: #d9469b;
    --magenta-soft: #e27ab8;
    --peach: #f2b98a;
    --amber: #e7a93e;
    --lavender: #d8c2dc;
    --ink: #1c1c1e;
    --radius: 24px;
  }
  * { box-sizing: border-box; margin: 0; padding: 0; }
  html, body {
    width: 1200px; height: 900px; overflow: hidden;
    background: var(--page);
    font-family: "Michroma", "Helvetica Neue", Arial, sans-serif;
  }
  .canvas {
    position: relative; width: 1200px; height: 900px;
    display: flex; align-items: center; justify-content: center; gap: 40px;
  }
  .card {
    position: relative; width: 550px; height: 314px;
    border-radius: var(--radius); overflow: hidden;
    box-shadow: 0 6px 18px rgba(0,0,0,0.18);
  }
  .card-art { position: absolute; inset: 0; width: 100%; height: 100%; }

  /* Front */
  .front-wordmark {
    position: absolute; right: 34px; top: 92px;
    color: var(--magenta); text-transform: uppercase;
    font-size: 15px; line-height: 1.35; letter-spacing: 0.06em; text-align: right;
  }
  .front-wordmark .monogram {
    display: block; font-size: 64px; line-height: 1; letter-spacing: 0.02em; margin-bottom: 8px;
  }

  /* Back */
  .back-wordmark {
    position: absolute; right: 70px; top: 26px;
    color: var(--ink); text-transform: uppercase;
    font-size: 10px; line-height: 1.35; letter-spacing: 0.06em; text-align: left;
  }
  .back-wordmark .monogram {
    display: block; font-size: 50px; line-height: 1; letter-spacing: 0.02em; margin-bottom: 6px;
  }
  .contact {
    position: absolute; right: 28px; bottom: 26px;
    color: var(--ink); text-transform: uppercase; font-size: 9.5px; letter-spacing: 0.02em;
    text-align: right; line-height: 1.6;
  }
  .contact .business-name { font-size: 10.5px; -webkit-text-stroke: 0.35px var(--ink); }
  .contact .address { margin-bottom: 16px; }
  .contact-row { display: flex; justify-content: flex-end; align-items: center; gap: 16px; }
  .contact-item { display: inline-flex; align-items: center; gap: 5px; }
  .contact-item svg { width: 11px; height: 11px; flex: none; }
  .social-square { width: 10px; height: 10px; background: var(--ink); border-radius: 2px; flex: none; }
  .website { font-size: 11px; -webkit-text-stroke: 0.35px var(--ink); text-align: left; }
  .contact-bottom { text-align: left; margin-top: 6px; }
</style>
</head>
<body>
<main class="canvas">

  <section class="card card-front" aria-label="Business card front">
    <svg class="card-art" viewBox="0 0 550 314" preserveAspectRatio="none">
      <defs>
        <linearGradient id="droplets-front" x1="0" y1="0" x2="1" y2="1">
          <stop offset="0" stop-color="#7d7d81"/>
          <stop offset="0.45" stop-color="#c4c4c7"/>
          <stop offset="1" stop-color="#a4a4a8"/>
        </linearGradient>
        <linearGradient id="butterfly-band" x1="0" y1="0" x2="0" y2="1">
          <stop offset="0" stop-color="#eadfe2"/>
          <stop offset="0.4" stop-color="#f2b98a"/>
          <stop offset="1" stop-color="#e8a06a"/>
        </linearGradient>
        <linearGradient id="blossom-band" x1="0" y1="0" x2="0" y2="1">
          <stop offset="0" stop-color="#e27ab8"/>
          <stop offset="1" stop-color="#d9469b"/>
        </linearGradient>
      </defs>
      <rect width="550" height="314" fill="url(#droplets-front)" role="img" aria-label="Black and white macro photograph of water droplets"/>
      <polygon points="150,0 235,0 175,314 80,314" fill="url(#butterfly-band)" role="img" aria-label="Photograph of a swallowtail butterfly on a blossom, tinted peach"/>
      <polygon points="235,0 300,0 240,314 175,314" fill="url(#blossom-band)" opacity="0.9" role="img" aria-label="Photograph of pink flower blossoms"/>
      <polygon points="300,0 345,0 285,314 240,314" fill="var(--lavender)" opacity="0.75" role="img" aria-label="Lavender tinted strip of the blossom photograph"/>
    </svg>
    <div class="front-wordmark">
      <span class="monogram">DH</span>
      Dorian<br>Hallet<br>Photography
    </div>
  </section>

  <section class="card card-back" aria-label="Business card back">
    <svg class="card-art" viewBox="0 0 550 314" preserveAspectRatio="none">
      <defs>
        <linearGradient id="droplets-back" x1="0" y1="0" x2="1" y2="1">
          <stop offset="0" stop-color="#b9b9bc"/>
          <stop offset="0.5" stop-color="#e4e4e6"/>
          <stop offset="1" stop-color="#cfcfd2"/>
        </linearGradient>
      </defs>
      <rect width="550" height="314" fill="url(#droplets-back)" role="img" aria-label="Soft grey photograph of water droplets"/>
      <polygon points="0,0 150,0 50,314 0,314" fill="#c9c9cc" role="img" aria-label="Grey bokeh photograph strip"/>
      <polygon points="150,0 195,0 110,314 50,314" fill="var(--amber)" opacity="0.85" role="img" aria-label="Amber tinted strip of a sparkling water photograph"/>
      <polygon points="195,0 260,0 175,314 110,314" fill="var(--magenta)" opacity="0.85" role="img" aria-label="Magenta tinted strip of a sparkling water photograph"/>
    </svg>

    <div class="back-wordmark">
      <span class="monogram">DH</span>
      Dorian<br>Hallet<br>Photography
    </div>

    <div class="contact">
      <p class="business-name">Dorian Hallet Photography</p>
      <p class="address">728 Maple Brook CT, Cedar Hollow,<br>NC 27999</p>
      <div class="contact-row">
        <span class="contact-item">
          <svg viewBox="0 0 12 12" aria-hidden="true"><rect x="0.5" y="0.5" width="11" height="11" rx="2" fill="var(--ink)"/><path d="M2.5 4 L6 6.5 L9.5 4 M2.5 4 H9.5 V8.5 H2.5 Z" fill="none" stroke="#fff" stroke-width="0.9"/></svg>
          dorian@dorianhallet.com
        </span>
        <span class="contact-item"><span class="social-square"></span>halletphoto</span>
      </div>
      <div class="contact-bottom">
        <span class="contact-item">
          <svg viewBox="0 0 12 12" aria-hidden="true"><rect x="0.5" y="0.5" width="11" height="11" rx="2" fill="var(--ink)"/><path d="M3.4 2.8 C3 3 2.7 3.6 3 4.6 C3.6 6.6 5.4 8.4 7.4 9 C8.4 9.3 9 9 9.2 8.6 L8 7.4 L7 7.9 C6 7.4 4.6 6 4.1 5 L4.6 4 Z" fill="#fff"/></svg>
          (555) 555-0148
        </span>
        <p class="website">www.dorianhallet.com</p>
      </div>
    </div>
  </section>

</main>
</body>
</html>
```